BRIM! Card

The single side "business card" will be utilized to write down product information for our customers. The card needs to include our logo in josefin font and read BRIM! on the front. Our brand colors are espresso brown and copper. The back needs to be white (blank) to allow us to write information down. We want modern, bold, clean and fun.
I have attached a copy of our logo but you do not have to utilize exactly as shown.

```html
<!DOCTYPE html>
<html lang="en">
<head>
<meta charset="utf-8">
<title>BRIM! Card</title>
<link rel="stylesheet" href="https://fonts.googleapis.com/css2?family=Josefin+Sans:wght@300;400;600&display=swap">
<style>
  :root {
    --backdrop: #2b2927;
    --card-blush: #f1dccb;
    --card-blush-light: #f6e6d8;
    --espresso: #6b4a1f;
    --copper: #c98a5c;
  }
  * { margin: 0; padding: 0; box-sizing: border-box; }
  html, body {
    width: 1200px;
    height: 800px;
    overflow: hidden;
  }
  body {
    background: var(--backdrop);
    display: flex;
    align-items: center;
    justify-content: center;
    font-family: "Josefin Sans", sans-serif;
  }
  .business-card {
    width: 840px;
    height: 480px;
    background: linear-gradient(160deg, var(--card-blush-light), var(--card-blush));
    border-radius: 4px;
    display: flex;
    flex-direction: column;
    align-items: center;
    justify-content: center;
    padding-top: 40px;
  }
  .headline {
    font-weight: 600;
    font-size: 200px;
    line-height: 1;
    letter-spacing: 2px;
    color: var(--espresso);
  }
  .brand {
    margin-top: 56px;
    text-align: center;
    color: var(--copper);
  }
  .brand-name {
    font-weight: 300;
    font-size: 36px;
    letter-spacing: 3px;
    line-height: 1;
  }
  .brand-tagline {
    margin-top: 8px;
    font-weight: 300;
    font-size: 13px;
    letter-spacing: 1px;
  }
</style>
</head>
<body>
  <main class="business-card">
    <h1 class="headline">BRIM!</h1>
    <div class="brand">
      <p class="brand-name">lumens</p>
      <p class="brand-tagline">Jewelry &amp; Design Studio</p>
    </div>
  </main>
</body>
</html>
```